Building company business card

Design and print business cards for BREVOTA PTY LTD.
A residantial homes building company.
Pixel Forge already designed the company Logo.

```html
<!DOCTYPE html>
<html lang="en">
<head>
<meta charset="utf-8">
<title>BREVOTA PTY LTD – Business Card</title>
<link rel="stylesheet" href="https://fonts.googleapis.com/css2?family=Lato:wght@400;700;900&display=swap">
<style>
  :root {
    --navy: #0f2170;
    --gold: #b8892e;
    --ink: #3a3a3a;
    --paper: #ffffff;
    --cream: #f1ebe0;
    --stage: #1c1c1e;
  }
  * { margin: 0; padding: 0; box-sizing: border-box; }
  html, body { width: 1200px; height: 800px; overflow: hidden; }
  body {
    background: var(--stage);
    font-family: "Lato", Arial, sans-serif;
    position: relative;
  }
  .card {
    position: absolute;
    top: 235px;
    width: 525px;
    height: 300px;
    overflow: hidden;
    box-shadow: 0 10px 30px rgba(0,0,0,.45);
  }
  .card--front { left: 50px; background: var(--paper); }
  .card--back  { left: 625px; background: var(--navy); }

  .front-texture {
    position: absolute; inset: 0;
    background: linear-gradient(120deg, var(--paper) 0%, var(--cream) 35%, var(--paper) 55%, var(--cream) 80%, var(--paper) 100%);
    opacity: .7;
  }
  .brand-name {
    position: absolute;
    left: 40px; top: 38px;
    font-weight: 900;
    font-size: 78px;
    line-height: 1;
    letter-spacing: 1px;
    color: var(--navy);
  }
  .person {
    position: absolute;
    left: 150px; top: 124px;
    text-align: right;
    width: 260px;
    color: var(--gold);
  }
  .person__name { font-weight: 700; font-size: 17px; letter-spacing: .3px; }
  .person__role { font-size: 14px; margin-top: 2px; }

  .rule { position: absolute; height: 1.5px; background: var(--navy); }
  .rule--main { left: 150px; right: 20px; top: 176px; }
  .rule--address { left: 22px; width: 170px; top: 196px; }

  .contacts {
    position: absolute;
    right: 22px; top: 186px;
    list-style: none;
    font-size: 13px;
    line-height: 19px;
    color: var(--ink);
    text-align: right;
  }
  .contacts li { display: flex; justify-content: flex-end; align-items: center; gap: 6px; }
  .contacts svg { width: 11px; height: 11px; fill: var(--gold); }

  .address {
    position: absolute;
    left: 22px; top: 202px;
    font-size: 12.5px;
    line-height: 17px;
    color: var(--ink);
  }
  .address__company { color: var(--navy); font-size: 12.5px; }

  .back-brand {
    position: absolute;
    inset: 0;
    display: flex;
    align-items: center;
    justify-content: center;
    gap: 14px;
  }
  .back-brand__mark { width: 30px; height: 30px; background: var(--gold); }
  .back-brand__name {
    font-weight: 900;
    font-size: 56px;
    color: var(--paper);
    letter-spacing: 1px;
  }
</style>
</head>
<body>
  <section class="card card--front" aria-label="Business card front">
    <div class="front-texture" role="img" aria-label="Soft cream diagonal background texture"></div>
    <div class="brand-name">BREVOTA</div>
    <div class="person">
      <div class="person__name">DORIAN (Dee) HALLOWAY</div>
      <div class="person__role">Director</div>
    </div>
    <div class="rule rule--main"></div>
    <ul class="contacts">
      <li>0412 555 018
        <svg viewBox="0 0 12 12"><path d="M3 1l2 2-1 1.5a6 6 0 003.5 3.5L9 7l2 2-1.5 1.8C5 10.5 1.5 7 1.2 2.5z"/></svg></li>
      <li>0412 555 018
        <svg viewBox="0 0 12 12"><path d="M3.5 0h5a1 1 0 011 1v10a1 1 0 01-1 1h-5a1 1 0 01-1-1V1a1 1 0 011-1zm.5 1.5v8h4v-8z"/></svg></li>
      <li>0418 555 027
        <svg viewBox="0 0 12 12"><path d="M3.5 0h5a1 1 0 011 1v10a1 1 0 01-1 1h-5a1 1 0 01-1-1V1a1 1 0 011-1zm.5 1.5v8h4v-8z"/></svg></li>
      <li>dh@brevota-pl.com
        <svg viewBox="0 0 12 12"><path d="M0 2h12v8H0zm1 1l5 3.5L11 3z"/></svg></li>
      <li>brevota-pl.com
        <svg viewBox="0 0 12 12"><path d="M6 0a6 6 0 110 12A6 6 0 016 0zm0 1.2a4.8 4.8 0 100 9.6 4.8 4.8 0 000-9.6zM1.5 5.4h9v1.2h-9zM5.4 1h1.2v10H5.4z"/></svg></li>
    </ul>
    <div class="rule rule--address"></div>
    <div class="address">
      <div class="address__company">BREVOTA PTY LTD</div>
      <div>PO Box 248</div>
      <div>Kewbridge, Vic 3999</div>
      <div>CDB- U 40518</div>
      <div>ABN- 51 824 900 162</div>
    </div>
  </section>

  <section class="card card--back" aria-label="Business card back">
    <div class="back-brand">
      <span class="back-brand__mark"></span>
      <span class="back-brand__name">BREVOTA</span>
    </div>
  </section>
</body>
</html>
```